The Gilded Otter Espresso Nook Coffee Card

would like a coffee card designed for our café. Most cards are so boring and I need to stand out from the crowd (The Gilded Otter ). I require our logo on one side or the business name also a place for people to write their name and mobile number (collecting data base) and on the back the following
customer gets a stamp for the 1st three coffees purchased, on the 3rd one they get a free upsize. another 2 stamps and on the 3rd one (6) gets a free coffee, another 2 stamps and the customer gets another upsize (9th coffee purchased) and on the 10th card they recivie a voucher for a free pizza.
small print | one free pizza for dinner dining (not available for takeaways and must book), Cant be used with any other offers, opts in to hear from the herd if there is a deal on. cant trade for cash or gift

```html
<!DOCTYPE html>
<html lang="en">
<head>
<meta charset="utf-8">
<title>The Gilded Otter Espresso Nook – Coffee Card</title>
<link rel="stylesheet" href="https://fonts.googleapis.com/css2?family=Oswald:wght@600;700&family=Roboto+Condensed:wght@300;400&family=Roboto:wght@400&display=swap">
<style>
  :root {
    --page: #d9d9d9;
    --card-front: #ffffff;
    --card-back: #2a2929;
    --ink: #111111;
    --ink-soft: #333333;
    --cup: #ffffff;
    --pizza-crust: #e0822f;
    --pizza-sauce: #c9541f;
    --shadow: rgba(0,0,0,0.28);
  }
  * { box-sizing: border-box; margin: 0; padding: 0; }
  html, body { width: 1125px; height: 1200px; overflow: hidden; }
  body { background: var(--page); position: relative; font-family: "Roboto Condensed", sans-serif; }

  .card {
    position: absolute; left: 150px; width: 825px; height: 470px;
    border-radius: 28px; box-shadow: 0 4px 10px var(--shadow);
  }
  .card--front { top: 106px; background: var(--card-front); }
  .card--back { top: 622px; background: var(--card-back); }

  .brand-name {
    position: absolute; left: 0; right: 0; top: 32px; text-align: center;
    font-family: "Oswald", "Arial Narrow", sans-serif; font-weight: 700;
    font-size: 76px; line-height: 1.2; color: var(--ink); letter-spacing: -1px;
    white-space: nowrap;
  }
  .brand-rule { position: absolute; left: 187px; width: 450px; top: 138px; height: 1.5px; background: var(--ink-soft); }
  .brand-tagline {
    position: absolute; left: 0; right: 0; top: 150px; text-align: center;
    font-weight: 300; font-size: 27px; line-height: 32px; color: var(--ink); letter-spacing: 0.5px;
    white-space: nowrap;
  }
  .field-label { position: absolute; left: 65px; top: 272px; font-size: 21px; font-weight: 400; color: var(--ink); white-space: nowrap; }
  .field-line { position: absolute; left: 65px; width: 694px; top: 308px; border-top: 1.5px dotted var(--ink); }
  .locations {
    position: absolute; left: 0; right: 0; top: 378px; text-align: center;
    font-weight: 300; font-size: 22px; color: var(--ink); white-space: nowrap;
  }

  .stamp { position: absolute; }
  .stamp svg { display: block; }
  .stamp--plain svg { width: 86px; height: 69px; }
  .stamp--reward svg { width: 112px; height: 88px; }
  .reward-label {
    position: absolute; left: 2px; width: 84px; top: 12px; text-align: center;
    font-family: "Oswald", "Arial Narrow", sans-serif; font-weight: 700; color: var(--ink);
    line-height: 0.95; white-space: nowrap;
  }
  .reward-label .big { display: block; font-size: 27px; }
  .reward-label .small { display: block; font-size: 17px; }

  .pizza { position: absolute; left: 614px; top: 200px; width: 106px; height: 112px; }
  .pizza-art {
    position: absolute; left: 0; top: 0; width: 104px; height: 104px; border-radius: 50%;
    background: radial-gradient(circle, var(--pizza-sauce) 55%, var(--pizza-crust) 60%);
  }
  .pizza-label {
    position: absolute; left: 0; width: 104px; top: 24px; text-align: center;
    font-family: "Oswald", "Arial Narrow", sans-serif; font-weight: 700; color: var(--ink);
    font-size: 25px; line-height: 0.95; white-space: nowrap;
  }

  .small-print {
    position: absolute; left: 0; right: 0; top: 352px; text-align: center;
    font-family: "Roboto", sans-serif; font-size: 13px; line-height: 16px; color: #ffffff;
    white-space: nowrap;
  }
</style>
</head>
<body>
<svg width="0" height="0" style="position:absolute">
  <symbol id="cup" viewBox="0 0 100 80">
    <path d="M2 4 H80 V42 Q80 78 44 78 H38 Q2 78 2 42 Z" fill="var(--cup)"/>
    <path d="M80 10 H88 Q97 10 97 24 Q97 38 86 38 H80" fill="none" stroke="var(--cup)" stroke-width="5"/>
  </symbol>
</svg>

<section class="card card--front" aria-label="Coffee card front">
  <h1 class="brand-name">THE GILDED OTTER</h1>
  <div class="brand-rule"></div>
  <p class="brand-tagline">ESPRESSO NOOK</p>
  <p class="field-label">NAME &amp; MOBILE NO</p>
  <div class="field-line"></div>
  <p class="locations">Harbourside 07 5500 1234 | Northpoint 07 5500 5678 | Riverbend 07 5500 9012</p>
</section>

<section class="card card--back" role="img" aria-label="Coffee card back, dark background with a faint pattern of herd silhouettes">
  <div class="stamp stamp--plain" style="left:78px;top:84px"><svg><use href="#cup"/></svg></div>
  <div class="stamp stamp--plain" style="left:213px;top:84px"><svg><use href="#cup"/></svg></div>
  <div class="stamp stamp--reward" style="left:340px;top:72px"><svg><use href="#cup"/></svg>
    <p class="reward-label"><span class="big">FREE</span><span class="small">UPSIZE</span></p></div>
  <div class="stamp stamp--plain" style="left:485px;top:84px"><svg><use href="#cup"/></svg></div>
  <div class="stamp stamp--reward" style="left:610px;top:76px"><svg><use href="#cup"/></svg>
    <p class="reward-label" style="top:16px"><span class="big">FREE</span><span class="small">COFFEE</span></p></div>

  <div class="stamp stamp--plain" style="left:80px;top:216px"><svg><use href="#cup"/></svg></div>
  <div class="stamp stamp--plain" style="left:213px;top:216px"><svg><use href="#cup"/></svg></div>
  <div class="stamp stamp--reward" style="left:340px;top:204px"><svg><use href="#cup"/></svg>
    <p class="reward-label"><span class="big">FREE</span><span class="small">UPSIZE</span></p></div>
  <div class="stamp stamp--plain" style="left:485px;top:216px"><svg><use href="#cup"/></svg></div>

  <div class="pizza">
    <div class="pizza-art" role="img" aria-label="Illustration of a pizza with a cut slice"></div>
    <p class="pizza-label">FREE<br>PIZZA</p>
  </div>

  <p class="small-print">One free pizza for dinner dining (not available for takeaways and must book),<br>Cant be used with any other offers • Opts in to hear from the herd if there is a deal on.<br>Cant trade for cash or gift</p>
</section>
</body>
</html>
```